Business Card Design

Please see my website www.lqvesting.com.au to for further information on my services and styling of my site

Project Deadline Extended
Reason: Deadline is extended to permit alterations to current designs or for any new submissions. Cheers

Industry/Entity Type

Business

Contact Information for Business Card

Marcus Theale
Empowerment Coach

'Live your passion'

marcus@lqvcoaching.com.au
0437518264
lqvcoaching.com.au

```html
<!DOCTYPE html>
<html lang="en">
<head>
<meta charset="utf-8">
<title>LQV Business Cards</title>
<link rel="stylesheet" href="https://fonts.googleapis.com/css2?family=Oswald:wght@500;700&family=Kaushan+Script&display=swap">
<style>
  :root {
    --stage: #e4e6e9;
    --card: #1c1c1c;
    --card-edge: #2a2a2a;
    --lime: #9fcf2b;
    --lime-dark: #6f9a14;
    --script-yellow: #e6e01c;
    --ink-white: #ffffff;
    --ink-black: #111111;
    --icon-blue: #2f6fc8;
  }
  html, body {
    margin: 0;
    width: 1200px;
    height: 960px;
    overflow: hidden;
    background: var(--stage);
  }
  .sheet {
    position: relative;
    width: 1200px;
    height: 960px;
  }
  .card {
    position: absolute;
    left: 220px;
    width: 760px;
    height: 420px;
    background: var(--card);
    border: 1px solid var(--card-edge);
    border-radius: 6px;
    box-shadow: 0 10px 30px rgba(0,0,0,.25);
    overflow: hidden;
  }
  .card--contact { top: 40px; }
  .card--brand { top: 500px; }

  /* contact side */
  .contact-ribbon {
    position: absolute;
    left: 0; top: 90px;
    width: 760px; height: 100px;
  }
  .brand-mark {
    position: absolute;
    right: 40px; top: 18px;
    display: flex; align-items: center; gap: 14px;
    font-family: "Oswald", sans-serif;
    font-weight: 700;
    font-size: 56px;
    line-height: 1;
    color: var(--lime);
  }
  .brand-mark__dot {
    width: 34px; height: 34px;
    border-radius: 50%;
    background: var(--ink-white);
  }
  .holder-name {
    position: absolute;
    left: 230px; top: 108px;
    width: 360px;
    text-align: center;
    font-family: "Oswald", sans-serif;
    font-weight: 700;
    font-size: 40px;
    line-height: 56px;
    letter-spacing: 1px;
    color: var(--ink-black);
    margin: 0;
  }
  .contact-block {
    position: absolute;
    left: 230px; top: 196px;
    width: 440px;
    font-family: "Oswald", sans-serif;
    font-weight: 700;
    color: var(--ink-white);
    text-align: center;
  }
  .contact-block__role,
  .contact-block__motto {
    margin: 0;
    font-size: 28px;
    line-height: 32px;
    letter-spacing: .5px;
  }
  .contact-list {
    list-style: none;
    margin: 10px 0 0;
    padding: 0 0 0 40px;
    text-align: left;
  }
  .contact-list li {
    display: flex; align-items: center; gap: 12px;
    font-size: 28px;
    line-height: 38px;
    font-weight: 500;
  }
  .contact-list svg { flex: none; }

  /* brand side */
  .tagline {
    position: absolute;
    margin: 0;
    font-family: "Kaushan Script", cursive;
    font-size: 32px;
    color: var(--script-yellow);
  }
  .tagline--top { left: 40px; top: 40px; }
  .tagline--bottom { right: 40px; bottom: 40px; }
  .brand-band {
    position: absolute;
    left: 0; top: 185px;
    width: 760px; height: 60px;
    background: var(--lime);
  }
  .brand-plate {
    position: absolute;
    left: 245px; top: 140px;
    width: 270px; height: 150px;
    box-sizing: border-box;
    border: 5px solid var(--ink-white);
    border-radius: 14px;
    background: var(--card);
    box-shadow: 0 0 24px rgba(255,255,255,.35);
    display: flex;
    align-items: center; justify-content: center;
    gap: 14px;
    font-family: "Oswald", sans-serif;
  }
  .brand-plate__name {
    font-weight: 700;
    font-size: 64px;
    line-height: 1;
    color: var(--lime);
  }
  .brand-plate__dot {
    width: 32px; height: 32px;
    border-radius: 50%;
    background: var(--ink-white);
  }
</style>
</head>
<body>
<main class="sheet">

  <section class="card card--contact" aria-label="Contact side">
    <svg class="contact-ribbon" viewBox="0 0 760 100" aria-hidden="true">
      <rect x="0" y="38" width="760" height="26" fill="var(--lime)"/>
      <polygon points="200,20 230,10 230,78 200,88 215,54" fill="var(--lime-dark)"/>
      <polygon points="620,20 590,10 590,78 620,88 605,54" fill="var(--lime-dark)"/>
      <rect x="230" y="10" width="360" height="68" fill="var(--lime)"/>
    </svg>
    <div class="brand-mark"><span>LQV</span><span class="brand-mark__dot"></span></div>
    <h1 class="holder-name">MARCUS THEALE</h1>
    <div class="contact-block">
      <p class="contact-block__role">EMPOWERMENT COACH</p>
      <p class="contact-block__motto">'LIVE YOUR PASSION'</p>
      <ul class="contact-list">
        <li>
          <svg width="26" height="26" viewBox="0 0 26 26" aria-hidden="true">
            <circle cx="13" cy="13" r="13" fill="var(--icon-blue)"/>
            <rect x="6" y="8" width="14" height="10" fill="#fff"/>
            <polyline points="6,8 13,14 20,8" fill="none" stroke="var(--icon-blue)" stroke-width="1.5"/>
          </svg>
          marcus@lqvcoaching.com.au
        </li>
        <li>
          <svg width="26" height="26" viewBox="0 0 26 26" aria-hidden="true">
            <circle cx="13" cy="13" r="13" fill="var(--icon-blue)"/>
            <path d="M8 7 l3 0 l1 4 l-2 1.5 a8 8 0 0 0 4.5 4.5 l1.5 -2 l4 1 l0 3 a2 2 0 0 1 -2 2 a13 13 0 0 1 -12 -12 a2 2 0 0 1 2 -2z" fill="#fff"/>
          </svg>
          0437518264
        </li>
        <li>
          <svg width="26" height="26" viewBox="0 0 26 26" aria-hidden="true">
            <circle cx="13" cy="13" r="13" fill="var(--icon-blue)"/>
            <polygon points="13,6 21,13 18,13 18,20 8,20 8,13 5,13" fill="#fff"/>
          </svg>
          lqvcoaching.com.au
        </li>
      </ul>
    </div>
  </section>

  <section class="card card--brand" aria-label="Brand side">
    <p class="tagline tagline--top">Strength and Conditioning Training</p>
    <div class="brand-band"></div>
    <div class="brand-plate">
      <span class="brand-plate__name">LQV</span>
      <span class="brand-plate__dot"></span>
    </div>
    <p class="tagline tagline--bottom">Empowerment Coaching</p>
  </section>

</main>
</body>
</html>
```